Meridale Counsel Corp Business Card design and layout

Meridale Counsel is a small, professional advisory firm specializing in business process consulting and advisory services. We are focused in the energy sector. The business card is to have a combination of blue shades and be professional and serious in nature. Investment banking, capital management, and professional service company card layouts should be used for similar templates

Target Market(s)

Medium to major corporations.

Industry/Entity Type

Consulting

Contact Information for Business Card

The card is to be professional looking in nature and must incorporate the company logo and name in some manner. A two sided design where the opposite side has a QR code and the logo is required.

Logo Text

Brastonhill Partners Inc.

Colors
0592cd
0455a3
3276b5
33a6d7
85cae6
85abd2
cee9f5
cedeed
ecf7fb

Requirements
Must have
• The card is to be professional and have space for employee, title, address, website, and phone numbers (office and cell). The layout must be some shades of blue.
Nice to have
• A space for embossing and/or some subtle gold highlights
Should not have
• Rainbow colours, unprofessional looking fonts (scribble, cursive writing)

```html
<!DOCTYPE html>
<html lang="en">
<head>
<meta charset="utf-8">
<title>Meridale Counsel Corp – Business Card</title>
<link rel="stylesheet" href="https://fonts.googleapis.com/css2?family=Lato:wght@300;400;700&display=swap">
<style>
  :root {
    --page-bg: #e7eaef;
    --card-white: #ffffff;
    --map-grey: #e9e9ea;
    --band-blue: #3a4fa3;
    --band-blue-light: #5f7cc4;
    --gold: #e8b23a;
    --ink-navy: #3a56a8;
    --ink-sky: #5aa8d8;
    --ink-muted: #8a98bf;
    --ink-mid: #4a5fa8;
  }
  html, body {
    margin: 0;
    width: 1200px;
    height: 801px;
    overflow: hidden;
    background: var(--page-bg);
    font-family: "Lato", Arial, sans-serif;
  }
  .card {
    position: absolute;
    left: 100px;
    top: 95px;
    width: 1000px;
    height: 612px;
    box-shadow: 0 10px 30px rgba(20, 30, 60, 0.22);
  }
  .card svg { display: block; width: 100%; height: 100%; }
  .name { font-weight: 700; font-size: 24px; fill: var(--ink-navy); }
  .title { font-weight: 400; font-size: 16px; fill: var(--ink-sky); letter-spacing: 0.5px; }
  .contact { font-weight: 300; font-size: 15px; fill: var(--ink-muted); }
  .contact-strong { font-weight: 400; font-size: 16px; fill: var(--ink-mid); }
  .company { font-weight: 700; font-size: 15px; fill: var(--ink-navy); letter-spacing: 0.3px; }
  .address { font-weight: 400; font-size: 16px; fill: var(--ink-sky); }
  .brand-name { font-weight: 700; font-size: 30px; fill: var(--ink-navy); letter-spacing: 1px; }
  .icon-box { fill: var(--ink-mid); }
  .icon-line { fill: none; stroke: #ffffff; stroke-width: 1.4; }
</style>
</head>
<body>
  <div class="card">
    <svg viewBox="0 0 765 468" xmlns="http://www.w3.org/2000/svg">
      <defs>
        <linearGradient id="mapTone" x1="0" y1="0" x2="1" y2="1">
          <stop offset="0" stop-color="#f2f2f3"/>
          <stop offset="1" stop-color="#e2e3e6"/>
        </linearGradient>
        <linearGradient id="bandTone" x1="0" y1="0" x2="1" y2="1">
          <stop offset="0" stop-color="var(--band-blue)"/>
          <stop offset="0.5" stop-color="var(--band-blue-light)"/>
          <stop offset="1" stop-color="var(--band-blue)"/>
        </linearGradient>
      </defs>

      <!-- card base -->
      <rect class="card-face" width="765" height="468" fill="var(--card-white)"/>

      <!-- upper-right world-map field -->
      <polygon class="map-field" role="img" aria-label="Faint dotted world map texture"
               points="120,0 765,0 765,440" fill="url(#mapTone)"/>

      <!-- diagonal band with gold edge -->
      <polygon class="diagonal-band" points="0,0 120,0 765,440 765,450 0,26" fill="url(#bandTone)"/>
      <line class="gold-rule" x1="122" y1="0" x2="765" y2="436" stroke="var(--gold)" stroke-width="1.6"/>

      <!-- bottom-left tab -->
      <path class="bottom-tab" d="M0 425 H338 Q350 425 356 432 L380 468 H0 Z" fill="var(--band-blue)"/>

      <!-- brand name -->
      <rect class="brand-mark" x="585" y="70" width="30" height="30" fill="var(--ink-sky)"/>
      <text class="brand-name" x="600" y="150" text-anchor="middle">MERIDALE</text>
      <text class="brand-name" x="600" y="186" text-anchor="middle" style="font-size:18px;letter-spacing:5px">COUNSEL CORP</text>

      <!-- person -->
      <text class="name" x="33" y="223">Martin Leclair, P.Eng</text>
      <text class="title" x="34" y="250">PRESIDENT</text>

      <!-- mobile -->
      <rect class="icon-box" x="34" y="270" width="22" height="21" rx="3"/>
      <rect class="icon-line" x="41" y="274" width="8" height="13" rx="1"/>
      <text class="contact" x="65" y="287">403-555-0142</text>

      <!-- web -->
      <rect class="icon-box" x="212" y="269" width="24" height="21" rx="3"/>
      <circle class="icon-line" cx="224" cy="279.5" r="6.5"/>
      <line class="icon-line" x1="217.5" y1="279.5" x2="230.5" y2="279.5"/>
      <ellipse class="icon-line" cx="224" cy="279.5" rx="2.8" ry="6.5"/>
      <text class="contact" x="248" y="284">www.meridalecounsel.com</text>

      <!-- office phone -->
      <rect class="icon-box" x="34" y="301" width="22" height="21" rx="3"/>
      <rect class="icon-line" x="39" y="305" width="5" height="13"/>
      <rect class="icon-line" x="46" y="308" width="6" height="10"/>
      <text class="contact-strong" x="66" y="318">+49 555 0183 27</text>

      <!-- email -->
      <rect class="icon-box" x="34" y="333" width="22" height="21" rx="3"/>
      <text x="45" y="349" text-anchor="middle" fill="#fff" font-size="15" font-family="Lato, Arial, sans-serif">@</text>
      <text class="contact" x="65" y="349">mleclair@meridalecounsel.com</text>

      <!-- company & address -->
      <text class="company" x="34" y="387">MERIDALE COUNSEL CORP</text>
      <text class="address" x="33" y="409">300, 418- 9th Ave, SW Calgary, AB T2P 1K5</text>
    </svg>
  </div>
</body>
</html>
```